New Chiropractic Office needs a fresh flyer design!

We need a flyer design for our chiropractic office for our hometown based chiropractic office called "Corvale Chiropractic" Dr. Martin Corvale provides chiropractic services including adjustments, xrays and wellness exercises with a fresh approach to chiropractic which focuses on getting your body aligned correctly to be a better you. We dont like to focus on coming in just for pain although that is what most people associate our operation with so we understand that comes with the territory. However we would like our flyers to express health and wellness rather than medical or pain. We would like our flyer to emphasize our "New Patient Special" which includes consultation, exam, xrays and first treatment for only $50. We also accept most insurance plans. Call for an appointment 618-390-2757.

Industry/Entity Type

Office

```html
<!DOCTYPE html>
<html lang="en">
<head>
<meta charset="utf-8">
<title>Corvale Chiropractic – New Patient Flyer</title>
<link href="https://fonts.googleapis.com/css2?family=Cinzel:wght@600&family=Yanone+Kaffeesatz:wght@400&family=Arimo:wght@400;700&family=Oswald:wght@400;500&display=swap" rel="stylesheet">
<style>
  :root{
    --paper:#e8eae5;
    --ink-grey:#5f625e;
    --navy:#0f2a70;
    --blue:#1d45a6;
    --cyan:#3fc7f0;
    --violet:#3b4bb3;
    --pink:#c85aa8;
    --white:#ffffff;
  }
  *{margin:0;padding:0;box-sizing:border-box}
  html,body{width:848px;height:1200px;overflow:hidden;background:var(--paper)}
  .flyer{position:relative;width:848px;height:1200px;overflow:hidden;background:var(--paper);font-family:"Arimo",Arial,sans-serif}
  .backdrop{position:absolute;inset:0}
  .brand{position:absolute;top:200px;left:0;width:848px;display:flex;align-items:center;justify-content:center;gap:16px}
  .brand-mark{width:34px;height:34px;border-radius:50%;background:var(--ink-grey)}
  .brand-name{font-family:"Arimo",Arial,sans-serif;font-weight:700;font-size:40px;color:var(--ink-grey);line-height:1}
  .doctor{position:absolute;top:330px;left:240px;font-family:"Cinzel",serif;font-weight:600;font-size:32px;color:var(--white);letter-spacing:.5px}
  .skeleton-art{position:absolute;left:118px;top:340px;width:290px;height:470px;border-radius:140px 140px 40px 40px;background:radial-gradient(circle at 55% 30%,rgba(160,200,240,.55),rgba(60,110,200,.25) 60%,transparent 75%)}
  .massage-photo{position:absolute;left:-10px;top:580px;width:292px;height:262px;border-radius:50%;border:7px solid #d9dde3;background:radial-gradient(circle at 50% 45%,#f1d4c6,#cfa48f 60%,#b28a7a)}
  .services{position:absolute;left:410px;top:393px;width:430px;border-left:3px solid var(--cyan);padding-left:10px;color:var(--white)}
  .services-intro{font-family:"Yanone Kaffeesatz",sans-serif;font-size:36px;line-height:40px}
  .rule{border-top:2px dotted rgba(255,255,255,.7);width:320px;margin:4px 0}
  .services-list{font-family:"Arimo",sans-serif;font-weight:700;font-size:46px;line-height:44px;padding:4px 0}
  .services-body{font-family:"Yanone Kaffeesatz",sans-serif;font-size:36px;line-height:34.5px;padding-top:12px}
  .offer{position:absolute;left:103px;top:856px}
  .offer-title{font-family:"Oswald",sans-serif;font-weight:500;font-size:38px;letter-spacing:3px;background:linear-gradient(90deg,var(--pink),var(--violet) 45%);-webkit-background-clip:text;background-clip:text;color:transparent;line-height:42px}
  .offer-items{font-family:"Arimo",sans-serif;font-size:57px;line-height:52px;color:var(--violet);letter-spacing:-1.5px}
  .offer-divider{position:absolute;left:522px;top:862px;height:140px;border-left:2px dotted var(--navy)}
  .badge{position:absolute;left:548px;top:800px;width:270px;height:270px}
  .badge-text{position:absolute;left:548px;top:858px;width:270px;text-align:center;color:var(--white);font-family:"Arimo",sans-serif;font-size:33px;line-height:33px}
  .badge-price{font-weight:700;font-size:40px;line-height:44px}
  .contact{position:absolute;left:0;top:1036px;width:848px;text-align:center;color:var(--white)}
  .contact-cta{font-family:"Arimo",sans-serif;font-size:37px;line-height:38px}
  .contact-phone{font-family:"Arimo",sans-serif;font-size:48px;line-height:50px;letter-spacing:1.5px}
  .contact-rule{width:756px;margin:8px auto 0;border-top:2px dotted rgba(255,255,255,.8)}
  .contact-address{font-family:"Oswald",sans-serif;font-size:25px;letter-spacing:8px;margin-top:8px}
</style>
</head>
<body>
<main class="flyer">
  <svg class="backdrop" width="848" height="1200" viewBox="0 0 848 1200" aria-hidden="true">
    <defs>
      <linearGradient id="deepBlue" x1="0" y1="0" x2="0" y2="1">
        <stop offset="0" stop-color="#17378c"/>
        <stop offset=".5" stop-color="#1d47a8"/>
        <stop offset="1" stop-color="#0f2a70"/>
      </linearGradient>
      <linearGradient id="skyBand" x1="0" y1="0" x2="1" y2="0">
        <stop offset="0" stop-color="#e6eef8"/>
        <stop offset=".6" stop-color="#cfe2f5"/>
        <stop offset="1" stop-color="#a9cdee"/>
      </linearGradient>
    </defs>
    <path d="M0 360 C220 330 420 270 848 295 L848 1200 L0 1200 Z" fill="#5d86cf"/>
    <path d="M0 372 C230 345 430 285 848 308 L848 1200 L0 1200 Z" fill="url(#deepBlue)"/>
    <path d="M0 815 C250 800 520 880 848 760 L848 1000 C600 1030 300 960 0 1012 Z" fill="url(#skyBand)"/>
    <path d="M0 1012 C300 960 600 1030 848 1000" fill="none" stroke="#ffffff" stroke-width="6"/>
    <path d="M0 1030 C300 985 600 1045 848 1018" fill="none" stroke="#2a5cc4" stroke-width="4"/>
  </svg>

  <header class="brand">
    <span class="brand-mark"></span>
    <h1 class="brand-name">Corvale Chiropractic</h1>
  </header>

  <h2 class="doctor">DR. MARTIN CORVALE</h2>

  <div class="skeleton-art" role="img" aria-label="Illustration of a translucent human figure with glowing spine, hand on sore neck"></div>
  <div class="massage-photo" role="img" aria-label="Photo of a relaxed woman receiving a shoulder massage"></div>

  <section class="services">
    <p class="services-intro">Provides Chiropractic Services</p>
    <div class="rule"></div>
    <p class="services-list">Adjustments<br>Xrays and<br>Wellness</p>
    <div class="rule"></div>
    <p class="services-body">Exercises with a fresh<br>Approach to Chiropractic<br>which focuses on<br>getting your body aligned<br>correctly to be<br>a better you</p>
  </section>

  <section class="offer">
    <p class="offer-title">NEW PATIENT SPECIAL</p>
    <p class="offer-items">Consultation<br>Exam &amp; Xrays</p>
  </section>
  <div class="offer-divider"></div>

  <svg class="badge" viewBox="0 0 270 270" aria-hidden="true">
    <g transform="translate(135 135)" fill="#4ea324">
      <rect x="-100" y="-100" width="200" height="200" rx="14"/>
      <rect x="-100" y="-100" width="200" height="200" rx="14" transform="rotate(30)"/>
      <rect x="-100" y="-100" width="200" height="200" rx="14" transform="rotate(60)"/>
    </g>
    <circle cx="135" cy="135" r="104" fill="#5cb42c"/>
    <circle cx="135" cy="135" r="96" fill="none" stroke="#3d8a1c" stroke-width="2"/>
  </svg>
  <p class="badge-text">First<br>Treatment<br>for only<br><span class="badge-price">$50</span></p>

  <footer class="contact">
    <p class="contact-cta">Call for an Appointment</p>
    <p class="contact-phone">618-390-2757</p>
    <div class="contact-rule"></div>
    <p class="contact-address">4810 LARKMOOR, BRENTON MI 48093</p>
  </footer>
</main>
</body>
</html>
```